IT Company WebPage Relaunch looking for modern and clean approach

We are looking to relaunch our website, to give it a more modern and clean look.
Company Background:
With nearly 20 years of industry expertise, we've been committed to delivering top-notch professional services and products, ensuring client success and efficiency. Our mission is to provide clients with talented human and technological resources, employing industry best practices for effective solutions. We envision becoming a pivotal player in Dominican Republic's Techonology sector, expanding our footprint across the Caribbean Central America and USA
Design Objectives:
1. Brand Identity: The website should reflect our brand identity based in our logo, color scheme, and overall aesthetic. Consistency with existing brand materials is essential.
2. User Experience: Prioritize user experience by ensuring easy navigation and intuitive layout. The website should be accessible and responsive across various devices and screen sizes.
3. Content Presentation: Present our content (text, images, videos) in a visually appealing and organized manner. Use creative layouts and typography to enhance readability and engagement.
4. Functionality: Implement necessary features and functionalities to support our business objectives. This may include contact form.
5. SEO Optimization: Design the website with search engine optimization (SEO) best practices in mind to improve visibility and ranking on search engine results pages (SERPs).
6. Multilanguage: Spanish and English
Pages and Sections:
1. Home Page:
o Welcome message/introduction
o Highlights of key products/services
o Clear navigation to other sections/pages
o Metrics (10 Satisfied customer) (Services provided in 5 countries) etc.
2. About Us:
o Company overview
o Mission, vision, and values
o Team/Staff profiles (tentative)
3. Products/Services:
o Our Partners
o Detailed descriptions of products/services offered
o Images/videos
4. Portfolio/Projects:
o Our Customers
o Case Studies
o Customer’s testimonials
5. Blog/News:
o Platform for sharing industry insights, updates, or company news
o Categories/tags for easy browsing
6. Contact Us:
o Contact form
o Company address, phone number, email
o Social media links
Design Preferences:
• Clean and modern design aesthetic
• Use of whitespace to enhance readability and visual appeal
• High-quality images and graphics
• Responsive to multiple devices
Technical Requirements:
• Compatibility with major web browsers (Chrome, Firefox, Safari, Edge)
• Compliance with web standards and best practices
Current Website:
https://www.corvantel.com.do
Note: The website should not be on Wordpress, we want an html/css website.

```html
<!DOCTYPE html>
<html lang="en">
<head>
<meta charset="utf-8">
<title>Corvantel – IT Consulting and Services</title>
<link href="https://fonts.googleapis.com/css2?family=Poppins:wght@400;500;600;700&family=Montserrat:wght@400;500;600&display=swap" rel="stylesheet">
<style>
:root{
  --ink:#2b2b2b;
  --text:#3a3a3a;
  --muted:#6b6b6b;
  --red:#e2332f;
  --red-dark:#c9222a;
  --orange:#f7941d;
  --orange-2:#f26a21;
  --cream:#fdf6ee;
  --dark:#1c1c1c;
  --dark-2:#2c2c2c;
  --field:#f0f0f0;
  --client:#2a3d8f;
  --white:#ffffff;
}
*{box-sizing:border-box;margin:0;padding:0}
html,body{width:1200px;height:4580px;overflow:hidden}
body{position:relative;background:var(--white);font-family:"Montserrat",sans-serif;color:var(--text)}
.abs{position:absolute}
h1,h2,h3,.brand-name,.stat-num{font-family:"Poppins",sans-serif;color:var(--ink)}
.eyebrow{font-family:"Poppins",sans-serif;font-weight:600;font-size:12px;letter-spacing:.5px;text-transform:uppercase;color:var(--muted)}
.btn{position:absolute;display:flex;align-items:center;justify-content:center;gap:8px;color:#fff;font-family:"Poppins",sans-serif;font-size:14px;text-transform:uppercase;background:linear-gradient(90deg,var(--orange),var(--orange-2));border-radius:8px 30px 30px 8px;box-shadow:0 6px 14px rgba(242,106,33,.25)}
.photo{position:absolute;overflow:hidden}
.blob-a{border-radius:42% 58% 52% 48% / 36% 44% 56% 64%}
.blob-b{border-radius:55% 45% 40% 60% / 45% 60% 40% 55%}
.dash{position:absolute;border:2px dashed var(--orange);opacity:.75}

/* header */
.brand{position:absolute;display:flex;align-items:center;gap:10px}
.brand-mark{width:44px;height:44px;border-radius:50%;background:var(--red)}
.brand-name{font-weight:700;font-size:30px;line-height:1;color:var(--ink)}
.brand-sub{font-size:10px;letter-spacing:.4px;color:var(--ink);margin-top:3px}
.nav{position:absolute;top:30px;right:84px;display:flex;gap:16px;align-items:center;font-family:"Poppins",sans-serif;font-size:14px;font-weight:500;color:var(--ink)}
.nav svg{width:14px;height:14px;fill:var(--red)}

/* hero */
.cream{position:absolute;left:0;top:440px;width:1200px;height:861px;background:var(--cream)}
.cream-top{position:absolute;left:0;top:0;width:1200px;height:700px}
.hero h1{position:absolute;left:76px;top:228px;font-size:54px;line-height:57px;font-weight:700;width:560px}
.hero p{position:absolute;left:76px;top:410px;width:520px;font-size:15px;line-height:23px}

/* services */
.service{position:absolute;left:612px;width:520px;display:flex;gap:22px}
.service svg{flex:0 0 56px;height:56px;stroke:var(--ink);fill:none;stroke-width:2}
.service h3{font-size:19px;font-weight:600;margin-bottom:6px}
.service p{font-size:14px;line-height:22px}

/* partners */
.badge{position:absolute;top:1458px;width:208px;height:65px;border-radius:10px 30px 30px 10px;background:#f4f4f4;box-shadow:0 8px 18px rgba(0,0,0,.08)}
.badge span{position:absolute;left:50%;top:50%;transform:translate(-50%,-50%);width:110px;height:18px;border-radius:9px;background:#d9d9d9}

/* about */
.about-band{position:absolute;left:0;top:1668px;width:1200px;height:409px;background:linear-gradient(90deg,var(--red),var(--red-dark))}
.about .eyebrow,.about h2,.about p{color:#fff}

/* customers */
.client{position:absolute;transform:translateX(-50%);display:flex;align-items:center;gap:8px;font-family:"Montserrat",sans-serif;font-weight:600;font-size:17px;color:var(--client);white-space:nowrap}
.client i{width:20px;height:20px;background:var(--client);border-radius:4px;display:block}

/* stats */
.stat-num{position:absolute;left:612px;font-size:76px;font-weight:700;line-height:1;color:var(--orange-2)}
.stat h3{position:absolute;left:612px;font-size:23px;font-weight:600}
.stat p{position:absolute;left:612px;font-size:14px;line-height:22px}

/* testimonial */
.testi-red{position:absolute;left:0;top:3115px;width:300px;height:480px;background:var(--red)}
.testi-dark{position:absolute;left:66px;top:3115px;width:890px;height:480px;background:linear-gradient(180deg,var(--dark-2),var(--dark));border-radius:0 0 0 70px}
.testi .eyebrow{color:#fff}
.testi h2{color:#fff}
.stars{position:absolute;left:160px;top:3462px;display:flex;gap:4px}
.stars svg{width:22px;height:22px;fill:var(--orange-2)}
.dots{position:absolute;left:168px;top:3528px;display:flex;gap:16px}
.dots span{width:13px;height:13px;border-radius:50%;background:#fff}
.dots span:first-child{background:var(--orange-2)}

/* contact */
.field-label{position:absolute;left:286px;font-family:"Poppins",sans-serif;font-weight:600;font-size:14px;color:var(--ink)}
.field{position:absolute;left:286px;width:628px;background:var(--field);font-size:13px;color:#8a8a8a;padding:0 18px;display:flex}

/* footer */
.footer{position:absolute;left:0;top:4174px;width:1200px;height:406px}
.footer h4{font-family:"Poppins",sans-serif;font-weight:500;font-size:19px;color:#fff}
.footer li{color:#cfcfcf;font-size:13px;list-style:none}
.foot-col{position:absolute;top:125px}
.foot-col ul{margin-top:24px;display:flex;flex-direction:column;gap:14px}
.contact-item{display:flex;gap:10px;margin-top:20px;color:#fff}
.contact-item svg{width:16px;height:16px;fill:var(--orange-2);flex:0 0 16px}
.contact-item b{display:block;font-size:12px;font-weight:600;color:#fff}
.contact-item span{font-size:13px;color:#cfcfcf}
</style>
</head>
<body>

<header>
  <div class="brand" style="left:76px;top:16px">
    <span class="brand-mark"></span>
    <div><div class="brand-name">CORVANTEL</div><div class="brand-sub">IT CONSULTING AND SERVICES</div></div>
  </div>
  <nav class="nav">
    <svg viewBox="0 0 16 16"><path d="M8 1 0 8h2v7h4v-5h4v5h4V8h2z"/></svg>
    <span>About Us</span><span>Our Partners</span><span>Portfolio</span><span>Contact Us</span>
  </nav>
</header>

<svg class="cream-top abs" viewBox="0 0 1200 700" preserveAspectRatio="none" aria-hidden="true">
  <path d="M0 660 C 200 640 430 720 560 640 C 660 580 650 320 760 180 L 1200 180 L1200 700 L0 700Z" fill="#fdf6ee"/>
</svg>
<div class="cream"></div>
<svg class="abs" style="left:960px;top:120px" width="240" height="495" viewBox="0 0 240 495" aria-hidden="true">
  <path d="M240 0 C 160 30 70 80 30 170 C -10 260 20 380 100 440 C 150 480 200 495 240 490Z" fill="#e2332f"/>
  <path d="M60 200 C 40 300 90 420 220 460" stroke="#f7941d" stroke-width="2" stroke-dasharray="6 5" fill="none"/>
</svg>

<section class="hero">
  <h1>The Revolution Technology a Look into the Future</h1>
  <p>With a history of almost two decades in the market, Corvantel stands out for providing professional services</p>
  <div class="btn" style="left:76px;top:470px;width:142px;height:38px">Get Started</div>
  <div class="photo blob-a" role="img" aria-label="Developer working on a laptop with holographic data overlay" style="left:662px;top:82px;width:388px;height:478px;background:linear-gradient(135deg,#1b2f5a,#2f6fa8 55%,#0e1a33)"></div>
  <div class="photo" role="img" aria-label="Close-up of code on a laptop screen" style="left:888px;top:410px;width:170px;height:200px;border-radius:50% 50% 45% 55%;border:5px solid #fff;background:linear-gradient(135deg,#5b2d8f,#c23a7a 60%,#2a1a4a)"></div>
</section>

<section class="services">
  <div class="dash" style="left:78px;top:662px;width:300px;height:420px;border-radius:50% 40% 45% 55%;border-right-color:transparent;border-bottom-color:transparent"></div>
  <div class="photo blob-b" role="img" aria-label="Hands typing on a laptop with digital interface icons" style="left:106px;top:665px;width:400px;height:380px;background:linear-gradient(135deg,#0e2a5e,#2e6fd1 55%,#0b1633)"></div>
  <div class="photo" role="img" aria-label="IT consultant working at a computer" style="left:270px;top:1012px;width:180px;height:182px;border-radius:50% 45% 50% 45%;border:5px solid #fff;background:linear-gradient(135deg,#3c4f6e,#7e9ab8 60%,#27344a)"></div>

  <div class="eyebrow abs" style="left:612px;top:748px">Services</div>
  <h2 class="abs" style="left:612px;top:770px;font-size:44px;line-height:56px;font-weight:600">Think Big<br>Think Different</h2>

  <div class="service" style="top:898px">
    <svg viewBox="0 0 56 56"><rect x="6" y="12" width="36" height="24" rx="2"/><path d="M18 44h12M24 36v8M16 22l-4 3 4 3M32 22l4 3-4 3M26 19l-4 12"/><circle cx="44" cy="12" r="6" stroke="#f26a21"/></svg>
    <div><h3>Software Factory</h3><p>We specialize in providing tailored software talent, ensuring that each developer or team...</p></div>
  </div>
  <div class="service" style="top:988px">
    <svg viewBox="0 0 56 56"><circle cx="28" cy="18" r="8" stroke="#f26a21"/><path d="M6 38c6-2 10-2 16 0h10c3 0 3 4 0 4H22M6 46l10-2 18 0 14-10"/></svg>
    <div><h3>Service Management</h3><p>We redefine IT service management with solutions that combine cutting-edge technology and...</p></div>
  </div>
  <div class="service" style="top:1078px">
    <svg viewBox="0 0 56 56"><rect x="10" y="14" width="18" height="34"/><rect x="28" y="22" width="18" height="26"/><path d="M15 20h8M15 28h8M15 36h8M33 30h8M33 38h8M6 48h44"/></svg>
    <div><h3>Infrastrucure</h3><p>We have a comprehensive portfolio of infrastructure management and monitoring solutions...</p></div>
  </div>
  <div class="service" style="top:1168px">
    <svg viewBox="0 0 56 56"><path d="M28 6 10 13v13c0 12 8 20 18 24 10-4 18-12 18-24V13z"/><rect x="21" y="26" width="14" height="11" rx="2" stroke="#f26a21"/><path d="M24 26v-4a4 4 0 0 1 8 0v4" stroke="#f26a21"/></svg>
    <div><h3>Security</h3><p>We have leading strategic allies in the area of cybersecurity with their solid portfolio of integrated...</p></div>
  </div>
  <div class="btn" style="left:612px;top:1267px;width:138px;height:48px">View All</div>
</section>

<section class="partners">
  <div class="eyebrow abs" style="left:76px;top:1350px">Trusted</div>
  <h2 class="abs" style="left:76px;top:1370px;font-size:42px;font-weight:600">Our Partners</h2>
  <div class="badge" style="left:94px"><span></span></div>
  <div class="badge" style="left:361px"><span></span></div>
  <div class="badge" style="left:628px"><span></span></div>
  <div class="badge" style="left:894px"><span></span></div>
</section>

<section class="about">
  <div class="about-band"></div>
  <div class="eyebrow abs" style="left:76px;top:1746px">Introduction</div>
  <h2 class="abs" style="left:76px;top:1768px;font-size:42px;font-weight:600">About CORVANTEL</h2>
  <p class="abs" style="left:76px;top:1830px;width:520px;font-size:15px;line-height:22.5px">With a history of almost two decades in the market, Corvantel stands out for providing professional services and technological solutions that optimize its clients' processes, thus driving their growth. Our team is made up of experts in various areas, such as software development, service management, information security and API administration, guaranteeing a comprehensive and cutting-edge approach to each project.</p>
  <div class="btn" style="left:76px;top:2062px;width:130px;height:38px">Read More</div>
  <div class="dash" style="left:752px;top:1650px;width:448px;height:470px;border-radius:45% 55% 60% 40% / 40% 50% 50% 60%;border-left-color:transparent"></div>
  <div class="photo blob-b" role="img" aria-label="Hand touching a laptop with rising bar chart hologram" style="left:722px;top:1656px;width:450px;height:462px;background:linear-gradient(135deg,#2a2ab8,#4a6de0 45%,#9a4fb0 80%,#d9794a);box-shadow:0 20px 40px rgba(0,0,0,.25)"></div>
</section>

<section class="customers">
  <div class="eyebrow abs" style="left:76px;top:2173px">Valuable</div>
  <h2 class="abs" style="left:76px;top:2193px;font-size:42px;font-weight:600">Our Customer</h2>
  <div class="client" style="left:172px;top:2303px"><i></i>Orvanta Credit</div>
  <div class="client" style="left:386px;top:2303px"><i></i>Kestral Savings</div>
  <div class="client" style="left:600px;top:2303px"><i></i>Miravel Trust</div>
  <div class="client" style="left:813px;top:2303px"><i></i>Tellara Mobile</div>
  <div class="client" style="left:1026px;top:2303px"><i></i>Norvik Agency</div>
  <div class="client" style="left:172px;top:2413px"><i></i>Solenne Capital</div>
  <div class="client" style="left:386px;top:2413px"><i></i>Arbela Funds</div>
  <div class="client" style="left:600px;top:2413px"><i></i>Finora Group</div>
  <div class="client" style="left:813px;top:2413px"><i></i>Portavia Cargo</div>
  <div class="client" style="left:1026px;top:2413px"><i></i>Luxera Power</div>
</section>

<section class="stat">
  <div class="abs" style="left:188px;top:2715px;width:110px;height:110px;border-radius:50%;background:var(--orange)"></div>
  <div class="dash" style="left:210px;top:2590px;width:380px;height:370px;border-radius:40% 60% 50% 50%;border-top-color:transparent;border-right-color:transparent"></div>
  <div class="photo blob-a" role="img" aria-label="City skyline at dusk with glowing network arcs" style="left:214px;top:2575px;width:364px;height:372px;background:linear-gradient(160deg,#f0a0c0,#7a6ad0 45%,#2b3b6a 75%,#1a2238);box-shadow:0 20px 40px rgba(0,0,0,.2)"></div>
  <div class="stat-num" style="top:2582px">23k</div>
  <h3 style="top:2654px">Happy Customers</h3>
  <p style="top:2692px;width:375px">To be successful, each software solution must be deeply integrated into the existing technological environment.</p>
  <div class="stat-num" style="top:2782px">5+</div>
  <h3 style="top:2852px">Countries Served</h3>
  <p style="top:2891px;width:405px">Our global presence allows us to understand diverse market dynamics while offering localized expertise to ensure the success of our clients in each region.</p>
</section>

<section class="testi">
  <div class="testi-red"></div>
  <div class="testi-dark"></div>
  <div class="eyebrow abs" style="left:172px;top:3193px">Testimonial</div>
  <h2 class="abs" style="left:172px;top:3212px;font-size:42px;font-weight:600">What Our Client Say</h2>
  <svg class="abs" style="left:172px;top:3280px" width="126" height="80" viewBox="0 0 126 80" aria-hidden="true"><path d="M34 0C15 0 0 15 0 34s15 34 34 34c2 0 4 0 6-1L28 80h18l14-32c2-4 4-9 4-14C64 15 50 0 34 0Zm60 0C75 0 60 15 60 34s15 34 34 34c2 0 4 0 6-1L88 80h18l14-32c2-4 4-9 4-14 0-19-14-34-30-34Z" fill="#555"/></svg>
  <p class="abs" style="left:160px;top:3368px;width:430px;font-size:17px;line-height:26px;color:#fff">To be successful, each software solution must be deeply integrated into the existing technological environment.</p>
  <div class="stars">
    <svg viewBox="0 0 24 24"><path d="M12 2l3 7 7 .6-5.4 4.7L18.2 22 12 18l-6.2 4 1.6-7.7L2 9.6 9 9z"/></svg>
    <svg viewBox="0 0 24 24"><path d="M12 2l3 7 7 .6-5.4 4.7L18.2 22 12 18l-6.2 4 1.6-7.7L2 9.6 9 9z"/></svg>
    <svg viewBox="0 0 24 24"><path d="M12 2l3 7 7 .6-5.4 4.7L18.2 22 12 18l-6.2 4 1.6-7.7L2 9.6 9 9z"/></svg>
    <svg viewBox="0 0 24 24"><path d="M12 2l3 7 7 .6-5.4 4.7L18.2 22 12 18l-6.2 4 1.6-7.7L2 9.6 9 9z"/></svg>
    <svg viewBox="0 0 24 24"><path d="M12 2l3 7 7 .6-5.4 4.7L18.2 22 12 18l-6.2 4 1.6-7.7L2 9.6 9 9z"/></svg>
  </div>
  <div class="abs" style="left:160px;top:3492px;font-size:17px;color:#fff">John Doe</div>
  <div class="dots"><span></span><span></span><span></span></div>

  <svg class="abs" style="left:780px;top:3175px" width="420" height="385" viewBox="0 0 420 385" aria-hidden="true">
    <path d="M420 330 C 360 250 300 240 250 200 C 180 150 150 40 240 10 C 320 -20 390 60 420 110Z" fill="#e2332f"/>
    <path d="M10 120 C 20 60 60 20 120 10" stroke="#f7941d" stroke-width="2" stroke-dasharray="6 5" fill="none"/>
  </svg>
  <div class="photo blob-b" role="img" aria-label="Smiling client giving a thumbs up" style="left:730px;top:3262px;width:372px;height:392px;border:5px solid #fff;background:linear-gradient(160deg,#d9dde2,#b8c6cf 55%,#8fbfb8);box-shadow:0 16px 36px rgba(0,0,0,.2)"></div>
</section>

<section class="contact">
  <div class="eyebrow abs" style="left:0;width:1200px;text-align:center;top:3690px;color:var(--ink)">Contact</div>
  <h2 class="abs" style="left:0;width:1200px;text-align:center;top:3712px;font-size:36px;font-weight:600">Get In Touch With Us</h2>
  <div class="field-label" style="top:3784px">EMAIL*</div>
  <div class="field" style="top:3805px;height:57px;align-items:center">Enter email address</div>
  <div class="field-label" style="top:3882px">MESSAGE*</div>
  <div class="field" style="top:3904px;height:155px;padding-top:24px">Type your text</div>
  <div class="abs" style="left:614px;width:300px;text-align:right;top:4064px;font-size:13px;color:var(--ink)">0 to 4000 max characters</div>
  <div class="btn" style="left:531px;top:4085px;width:136px;height:48px">Send
    <svg width="16" height="16" viewBox="0 0 24 24" fill="#fff"><path d="M2 21 23 12 2 3v7l15 2-15 2z"/></svg></div>
</section>

<footer class="footer">
  <svg class="abs" style="left:0;top:0" width="1200" height="406" viewBox="0 0 1200 406" aria-hidden="true">
    <defs><linearGradient id="footGrad" x1="0" y1="0" x2="0" y2="1"><stop offset="0" stop-color="#262626"/><stop offset="1" stop-color="#111"/></linearGradient></defs>
    <path d="M0 30 Q0 0 60 0 L900 0 C 1060 0 1160 120 1200 300 L1200 406 L0 406Z" fill="url(#footGrad)"/>
  </svg>
  <div class="brand" style="left:76px;top:172px">
    <span class="brand-mark"></span>
    <div><div class="brand-name" style="color:#fff">CORVANTEL</div><div class="brand-sub" style="color:#fff">IT CONSULTING AND SERVICES</div></div>
  </div>
  <div class="foot-col" style="left:377px"><h4>Quick Links</h4><ul><li>Start</li><li>Solutions &amp; Services</li><li>Partners</li><li>About us</li></ul></div>
  <div class="foot-col" style="left:613px"><h4>Information</h4><ul><li>Privacy Policy</li><li>Terms &amp; Condition</li><li>Site Map</li></ul></div>
  <div class="foot-col" style="left:866px"><h4>Contact Us</h4>
    <div class="contact-item"><svg viewBox="0 0 24 24"><path d="M6.6 10.8a15 15 0 0 0 6.6 6.6l2.2-2.2c.3-.3.7-.4 1-.2 1.1.4 2.3.6 3.6.6.6 0 1 .4 1 1V20c0 .6-.4 1-1 1A17 17 0 0 1 3 4c0-.6.4-1 1-1h3.5c.6 0 1 .4 1 1 0 1.3.2 2.5.6 3.6.1.3 0 .7-.2 1z"/></svg><div><b>PHONE</b><span>809-555-0148</span></div></div>
    <div class="contact-item"><svg viewBox="0 0 24 24"><path d="M2 5h20v14H2zm2 2v.5l8 5 8-5V7z"/></svg><div><b>EMAIL</b><span>info@corvantel.com.do</span></div></div>
  </div>
  <div class="abs" style="left:76px;top:336px;width:1050px;height:1px;background:#3a3a3a"></div>
  <div class="abs" style="left:0;width:1200px;text-align:center;top:362px;font-size:13px;color:#fff">© 2024 CORVANTEL. All rights reserved.</div>
  <div class="abs" style="left:1028px;top:356px;display:flex;align-items:center;gap:10px;font-size:13px;color:#fff">
    <span style="width:30px;height:30px;border-radius:50%;background:#333;display:block"></span>ProLink</div>
</footer>

</body>
</html>
```